New Business Cards

We are a long time (57 years) independent pharmacy that needs a new look for a new generation. We are fast at what we do and don't have long lines to wait in. We are also more than a pharmacy as we carry lift chairs, walkers, ostomy supplies, wound care, nebulizers, and braces. I want to be able to use the look on facebook, twitter, postcards, letters, emails, and business cards. I want it to be something that when they see it they think Bluestone Corner Pharmacy.Our primary colors are red and blue. You can check out www.bluestonecornerpharmacy.net and www.friendwall.net/bluecornrx. We also are now a KPW contract holder.

The attached documents are some examples of things we like. and the jpg file is what we use now that does not work well for social media marketing or print marketing.

Target Market(s)

The primary audience we are looking at is going to be the 25 and older crowd.

Industry/Entity Type

Marketing

Font styles to use
Serif
Sans Serif

Colors
0255a3
ec2229

Requirements
Must have
• Name
Address
Facebook logo or address
contact info
Nice to have
• Twitter logo
KPW logo

```html
<!DOCTYPE html>
<html lang="en">
<head>
<meta charset="utf-8">
<title>Bluestone Corner Pharmacy – Business Card</title>
<link rel="stylesheet" href="https://fonts.googleapis.com/css2?family=Cinzel:wght@500&family=Open+Sans:wght@400;700&display=swap">
<style>
  :root {
    --brand-blue: #0255a3;
    --brand-blue-deep: #1c3f85;
    --brand-red: #ec2229;
    --brand-red-dark: #c81d24;
    --paper: #ffffff;
    --backdrop: #e2e2e2;
    --text-light: #ffffff;
  }
  * { margin: 0; padding: 0; box-sizing: border-box; }
  html, body {
    width: 1200px; height: 900px; overflow: hidden;
    background: var(--backdrop);
    font-family: "Open Sans", Arial, sans-serif;
  }
  .card {
    position: absolute; left: 150px; top: 195px;
    width: 900px; height: 510px;
    border-radius: 30px; overflow: hidden;
    background: var(--paper);
  }
  .card-header { position: absolute; inset: 0 0 auto 0; height: 248px; background: var(--paper); }
  .brand-mark {
    position: absolute; left: 62px; top: 56px;
    width: 140px; height: 140px; border-radius: 50%;
    background: var(--brand-red);
  }
  .brand-name {
    position: absolute; left: 232px; top: 104px;
    font-family: "Cinzel", "Times New Roman", serif;
    font-weight: 500; font-size: 31px; letter-spacing: 0.5px;
    color: var(--brand-blue); white-space: nowrap;
  }
  .accent-stripe {
    position: absolute; left: 0; right: 0; top: 240px; height: 24px;
    background: linear-gradient(180deg, var(--brand-red), var(--brand-red-dark));
  }
  .card-body {
    position: absolute; left: 0; right: 0; top: 264px; bottom: 0;
    background: linear-gradient(180deg, var(--brand-blue) 0%, var(--brand-blue-deep) 100%);
  }
  .person-name {
    position: absolute; left: 56px; top: 18px;
    font-weight: 700; font-size: 29px; color: var(--brand-red);
  }
  .person-title {
    position: absolute; left: 56px; top: 58px;
    font-size: 20px; color: var(--text-light);
  }
  .contact-list {
    position: absolute; left: 56px; top: 122px; list-style: none;
  }
  .contact-list li {
    display: flex; align-items: center; gap: 12px;
    height: 31px; font-size: 21px; color: var(--text-light);
  }
  .contact-list svg { width: 24px; height: 24px; fill: var(--brand-red); flex: none; }
  .partner-badge {
    position: absolute; right: 42px; top: 20px;
    width: 60px; height: 74px;
    background: var(--brand-blue-deep); border: 2px solid #7f9bc8;
  }
  .social-links { position: absolute; right: 42px; top: 108px; display: flex; gap: 6px; }
  .social-links span { width: 30px; height: 32px; border-radius: 4px; background: #4f82c7; }
  .social-links span + span { background: #3aa5df; }
</style>
</head>
<body>
  <div class="card">
    <header class="card-header">
      <div class="brand-mark" role="img" aria-label="Pharmacy emblem"></div>
      <div class="brand-name">Bluestone Corner Pharmacy</div>
    </header>
    <div class="accent-stripe"></div>
    <section class="card-body">
      <div class="person-name">Dana Whitfield</div>
      <div class="person-title">Managing Director</div>
      <ul class="contact-list">
        <li>
          <svg viewBox="0 0 24 24" aria-hidden="true"><path d="M12 3 2 12h3v9h5v-6h4v6h5v-9h3z"/></svg>
          PO Box 40517 AL 36990
        </li>
        <li>
          <svg viewBox="0 0 24 24" aria-hidden="true"><path d="M6.6 10.8a15 15 0 0 0 6.6 6.6l2.2-2.2c.3-.3.7-.4 1-.2 1.1.4 2.3.6 3.6.6.6 0 1 .4 1 1V20c0 .6-.4 1-1 1A17 17 0 0 1 3 4c0-.6.4-1 1-1h3.5c.6 0 1 .4 1 1 0 1.3.2 2.5.6 3.6.1.3 0 .7-.2 1z"/></svg>
          1555 318 702
        </li>
        <li>
          <svg viewBox="0 0 24 24" aria-hidden="true"><path d="M3 6h18v12H3zm2 2v.4l7 4.6 7-4.6V8l-7 4.5z"/></svg>
          dana@www.bluestonecornerpharmacy.net
        </li>
        <li>
          <svg viewBox="0 0 24 24" aria-hidden="true"><path d="M12 2a10 10 0 1 0 0 20 10 10 0 0 0 0-20zm6.9 9h-3a15 15 0 0 0-1.3-5.6A8 8 0 0 1 18.9 11zM12 4c.9 1.2 1.8 3.6 1.9 7h-3.8c.1-3.4 1-5.8 1.9-7zM9.4 5.4A15 15 0 0 0 8.1 11h-3a8 8 0 0 1 4.3-5.6zM5.1 13h3a15 15 0 0 0 1.3 5.6A8 8 0 0 1 5.1 13zM12 20c-.9-1.2-1.8-3.6-1.9-7h3.8c-.1 3.4-1 5.8-1.9 7zm2.6-1.4a15 15 0 0 0 1.3-5.6h3a8 8 0 0 1-4.3 5.6z"/></svg>
          www.bluestonecornerpharmacy.net
        </li>
      </ul>
      <div class="partner-badge" role="img" aria-label="Contract holder badge"></div>
      <div class="social-links" aria-label="Social profiles">
        <span></span><span></span>
      </div>
    </section>
  </div>
</body>
</html>
```